STI/STD Medical Clinic- Wellspring Crest Partners, Inc Website

We are a STI clinic in florida looking for a website. We want to be professional but also playful. We want a buildout similar to the website listed below as our clinic is very similar to theirs.

This is a great example of a clinic doing similar stuff as us. We obviously do not want their color scheme but their format and buildout work. Please see our logo attached for color schemes etc.

https://bluefernclinicmiami.org

Industry/Entity Type

Medical

Coding

Coded - Design and coding required

Number of Pages Required

5+ page

Font styles to use
Sans Serif

```html
<!DOCTYPE html>
<html lang="en">
<head>
<meta charset="utf-8">
<title>Wellspring Crest Partners</title>
<link href="https://fonts.googleapis.com/css2?family=Poppins:wght@400;500;600;700&display=swap" rel="stylesheet">
<style>
:root{
  --purple:#5b2ee6;
  --red:#ff4b4b;
  --blue:#1a86ff;
  --orange:#ff6a3d;
  --pink:#f23fc7;
  --ink:#3b3b3b;
  --body:#555;
  --white:#fff;
}
*{box-sizing:border-box;margin:0;padding:0}
html,body{width:1200px;height:4570px;overflow:hidden}
body{font-family:'Poppins',sans-serif;color:var(--body);background:#fff;position:relative}
.abs{position:absolute}
a{color:inherit;text-decoration:none}

.topbar{left:0;top:0;width:1200px;height:64px;background:linear-gradient(90deg,#3a4ce8,#5a2fe0);}
.social{display:flex;gap:14px;position:absolute;left:72px;top:22px}
.social span{width:20px;height:20px;border-radius:50%;background:rgba(255,255,255,.9);display:block}
.toplinks{position:absolute;right:72px;top:20px;color:#fff;font-size:16px}
.toplinks span{margin:0 10px;opacity:.8}

.hero{left:0;top:64px;width:1200px;height:691px;background:linear-gradient(180deg,#4c6a86 0%,#6e8aa0 35%,#3f5a56 70%,#6b5a3c 100%)}
.hero-shade{left:0;top:64px;width:1200px;height:691px;background:rgba(20,20,40,.35)}
.brand{left:75px;top:88px;display:flex;align-items:center;gap:12px;color:#fff;font-weight:700;font-size:52px;letter-spacing:1px}
.brand i{width:62px;height:62px;border-radius:50%;background:var(--pink);display:block}
.nav{right:75px;top:116px;display:flex;gap:38px;color:#fff;font-size:16px;font-weight:500}
.nav .on{color:var(--orange)}
.hero-title{left:0;top:300px;width:1200px;text-align:center;color:#fff;font-weight:700;font-size:52px;letter-spacing:1px}
.hero-sub{left:270px;top:366px;width:660px;text-align:center;color:#fff;font-size:21px;line-height:31px}
.btn{display:inline-block;border-radius:30px;color:#fff;font-weight:700;text-transform:uppercase;text-align:center}
.hero-btn{left:465px;top:458px;width:272px;height:55px;line-height:55px;background:var(--orange);font-size:16px}

.card{top:586px;width:328px;height:472px;border-radius:164px;color:#fff;text-align:center}
.card.prep{left:75px;background:var(--purple)}
.card.sti{left:437px;background:var(--red)}
.card.hiv{left:799px;background:var(--blue)}
.card .ic{width:133px;height:133px;border-radius:50%;background:#fff;margin:35px auto 0;display:flex;align-items:center;justify-content:center}
.card h3{font-size:30px;font-weight:700;margin-top:34px}
.card p{font-size:15px;line-height:28px;padding:0 28px;margin-top:16px}
.card .more{font-size:14px;font-weight:700;margin-top:18px;display:block}

.about-band{left:0;top:1163px;width:494px;height:532px;background:linear-gradient(180deg,#8a3be0,#c43a9a);border-top-right-radius:90px}
.photo{border-radius:90px}
.about-photo{left:75px;top:1223px;width:600px;height:527px;background:linear-gradient(180deg,#d9dfe4 0%,#e6e6e6 40%,#d43b3b 70%,#3a6ad9 100%)}
.dots{background-image:radial-gradient(circle,var(--blue) 2px,transparent 2.5px);background-size:14px 14px}
.h2{font-size:40px;font-weight:700;color:var(--ink);line-height:53px;text-transform:uppercase}
.copy{font-size:16px;line-height:34px;color:var(--body)}
.about-title{left:705px;top:1266px;width:440px}
.about-copy{left:705px;top:1383px;width:430px}
.btn-purple{background:var(--purple);width:179px;height:54px;line-height:54px;font-size:17px}

.services{left:0;top:1858px;width:1200px;height:613px;background:linear-gradient(100deg,#1f8cf0 0%,#7d6fc6 50%,#ff6e3a 100%)}
.services .h2{color:#fff;position:absolute;left:75px;top:150px}
.services .copy{color:#fff;position:absolute;left:75px;top:200px;width:430px}
.services .btn{position:absolute;left:75px;top:400px}
.svc{position:absolute;width:180px;text-align:center;color:#fff;font-weight:600;font-size:20px;letter-spacing:1px}
.svc i{display:block;width:88px;height:88px;border-radius:50%;background:#fff;border:3px solid var(--pink);margin:0 auto 14px}

.team-band{left:707px;top:2556px;width:493px;height:533px;background:linear-gradient(135deg,#c73aa8,#6a3ae0);border-top-left-radius:90px}
.team-photo{left:524px;top:2618px;width:600px;height:528px;background:linear-gradient(180deg,#e4e2dc 0%,#cfc6bb 40%,#27324e 75%,#1f2a44 100%)}
.team-title{left:76px;top:2662px;width:380px}
.team-copy{left:75px;top:2777px;width:430px}

.book{left:0;top:3249px;width:1200px;height:613px;background:linear-gradient(110deg,#5a36e6 0%,#a83fe0 50%,#f447c4 100%)}
.book .h2{color:#fff;position:absolute;left:75px;top:160px}
.book .copy{color:#fff;position:absolute;left:75px;top:270px;width:430px}
.field{position:absolute;background:#fff;border-radius:30px;color:#555;font-size:15px;padding-left:28px;line-height:60px}
.field.msg{border-radius:24px;line-height:26px;padding-top:16px}
.btn-orange{background:var(--orange);width:179px;height:54px;line-height:54px;font-size:17px}

.partner{top:3935px;height:56px;border-radius:28px;background:#e9e6f0}
.pager{left:566px;top:4043px;display:flex;gap:9px}
.pager i{width:10px;height:10px;border-radius:50%;background:#bbb;display:block}
.pager i:first-child{background:var(--purple)}

.footer{left:0;top:4108px;width:1200px;height:462px;background:linear-gradient(100deg,#ff4a55 0%,#c23ea0 55%,#6a3ae6 100%);color:#fff}
.footer .brand{position:absolute;left:75px;top:60px;font-size:52px}
.footer .about{position:absolute;left:75px;top:165px;width:320px;font-size:16px;line-height:28px}
.fcol{position:absolute;top:62px;font-size:16px;line-height:37px}
.fcol h4{font-size:17px;font-weight:700;margin-bottom:2px}
.fcol .sub{font-size:14px;font-weight:700;line-height:24px;margin-bottom:8px}
.crow{display:flex;gap:14px;font-size:15px;line-height:24px;margin-bottom:10px}
.crow b{flex:0 0 16px;height:16px;border-radius:50%;background:#fff;margin-top:4px}
.fsocial{display:flex;gap:20px;margin-top:12px}
.fsocial span{width:22px;height:22px;border-radius:50%;background:#fff;display:block}
.fline{position:absolute;left:0;top:398px;width:1200px;height:1px;background:rgba(255,255,255,.3)}
.copyright{position:absolute;left:0;top:419px;width:1200px;text-align:center;font-size:14px}
</style>
</head>
<body>

<header class="abs topbar">
  <div class="social"><span></span><span></span><span></span><span></span><span></span></div>
  <div class="toplinks">Patient Portal<span>/</span>Patient Messaging App<span>/</span>Donate</div>
</header>

<div class="abs hero" role="img" aria-label="Aerial photo of a waterfront Florida city skyline"></div>
<div class="abs hero-shade"></div>
<div class="abs brand"><i></i>WCP</div>
<nav class="abs nav"><a class="on">Home</a><a>About</a><a>Meet The Team</a><a>Services</a><a>News</a><a>FAQs</a><a>Contact</a></nav>
<h1 class="abs hero-title">WELLSPRING CREST PARTNERS</h1>
<p class="abs hero-sub">Sed ut perspiciatis unde omnis iste natus error sit voluptatem accusantium doloremque laudantium.</p>
<a class="abs btn hero-btn">Book an Appointment</a>

<div class="abs card prep">
  <div class="ic"><svg width="60" height="60" viewBox="0 0 60 60" fill="none" stroke="#333" stroke-width="2.5"><rect x="12" y="10" width="32" height="42" rx="3"/><rect x="22" y="6" width="12" height="8" rx="2"/><circle cx="28" cy="32" r="9"/><path d="M28 27v10M23 32h10"/></svg></div>
  <h3>PrEP</h3>
  <p>Sed ut perspiciatis unde omnis iste natus error sit voluptatem acc usantium doloremque consequu ntur magni dolores eos.</p>
  <a class="more">LEARN MORE &rarr;</a>
</div>
<div class="abs card sti">
  <div class="ic"><svg width="64" height="64" viewBox="0 0 64 64" fill="none" stroke="#333" stroke-width="2.5"><circle cx="32" cy="32" r="13"/><circle cx="28" cy="29" r="3"/><circle cx="36" cy="36" r="2.5"/><path d="M32 6v9M32 49v9M6 32h9M49 32h9M13 13l7 7M44 44l7 7M51 13l-7 7M20 44l-7 7"/></svg></div>
  <h3>STI</h3>
  <p>Sed ut perspiciatis unde omnis iste natus error sit voluptatem acc usantium doloremque consequu ntur magni dolores eos.</p>
  <a class="more">LEARN MORE &rarr;</a>
</div>
<div class="abs card hiv">
  <div class="ic"><svg width="56" height="64" viewBox="0 0 56 64" fill="none" stroke="#333" stroke-width="2.5"><path d="M28 8c-8 0-12 6-10 14l20 36 6-6-16-30c-2-4-2-8 0-10M28 8c8 0 12 6 10 14L18 58l-6-6 16-30"/></svg></div>
  <h3>HIV</h3>
  <p>Sed ut perspiciatis unde omnis iste natus error sit voluptatem acc usantium doloremque consequu ntur magni dolores eos.</p>
  <a class="more">LEARN MORE &rarr;</a>
</div>

<section>
  <div class="abs about-band"></div>
  <div class="abs dots" style="left:500px;top:1625px;width:210px;height:150px"></div>
  <div class="abs photo about-photo" role="img" aria-label="Smiling doctor in a white coat holding a rainbow flag"></div>
  <h2 class="abs h2 about-title">About Wellspring Crest Partners</h2>
  <p class="abs copy about-copy">Sed ut perspiciatis unde omnis iste natus error sit voluptatem accusantium doloremque laudantium, totam rem aperiam, eaque ipsa quae ab illo inve ntore veritatis et quasi architecto beatae vitae dicta sunt explicabo.</p>
  <a class="abs btn btn-purple" style="left:705px;top:1580px">Read More</a>
</section>

<section class="abs services">
  <h2 class="h2">Our Services</h2>
  <p class="copy">Sed ut perspiciatis unde omnis iste natus error sit voluptatem accusantium doloremque laudantium, totam rem aperiam, eaque ipsa quae ab illo inve ntore veritatis et quasi architecto beatae vitae dicta sunt explicabo.</p>
  <a class="btn btn-purple">Read More</a>
  <div class="svc" style="left:517px;top:161px"><i></i>PrEP</div>
  <div class="svc" style="left:735px;top:161px"><i></i>PEP</div>
  <div class="svc" style="left:954px;top:161px"><i></i>HEPATITIS C</div>
  <div class="svc" style="left:517px;top:336px"><i></i>HIV</div>
  <div class="svc" style="left:735px;top:336px"><i></i>STI</div>
  <div class="svc" style="left:954px;top:336px"><i></i>TELEHEALTH</div>
</section>

<section>
  <div class="abs team-band"></div>
  <div class="abs dots" style="left:492px;top:3020px;width:210px;height:150px"></div>
  <div class="abs photo team-photo" role="img" aria-label="Clinic team in navy scrubs standing together"></div>
  <h2 class="abs h2 team-title">Meet the WCP Team</h2>
  <p class="abs copy team-copy">Sed ut perspiciatis unde omnis iste natus error sit voluptatem accusantium doloremque laudantium, totam rem aperiam, eaque ipsa quae ab illo inve ntore veritatis et quasi architecto beatae vitae dicta sunt explicabo.</p>
  <a class="abs btn btn-purple" style="left:76px;top:2975px">Read More</a>
</section>

<section class="abs book">
  <h2 class="h2">Book an<br>Appointment</h2>
  <p class="copy">Sed ut perspiciatis unde omnis iste natus error sit voluptatem accusantium doloremque laudantium, totam rem aperiam, eaque ipsa quae ab illo inve ntore veritatis et quasi architecto beatae vitae dicta sunt explicabo.</p>
  <div class="field" style="left:524px;top:102px;width:292px;height:60px">First Name</div>
  <div class="field" style="left:834px;top:102px;width:291px;height:60px">Last Name</div>
  <div class="field" style="left:524px;top:180px;width:292px;height:60px">Phone No</div>
  <div class="field" style="left:834px;top:180px;width:291px;height:60px">Subject</div>
  <div class="field" style="left:524px;top:258px;width:601px;height:60px">Email Address</div>
  <div class="field msg" style="left:524px;top:335px;width:601px;height:110px">Message</div>
  <a class="btn btn-orange" style="position:absolute;left:524px;top:457px">Read More</a>
</section>

<div class="abs partner" style="left:80px;width:170px"></div>
<div class="abs partner" style="left:365px;width:170px"></div>
<div class="abs partner" style="left:655px;width:170px"></div>
<div class="abs partner" style="left:940px;width:170px"></div>
<div class="abs pager"><i></i><i></i><i></i><i></i></div>

<footer class="abs footer">
  <div class="brand" style="display:flex;align-items:center;gap:12px;font-weight:700"><i style="width:56px;height:56px;border-radius:50%;background:#fff;display:block"></i>WCP</div>
  <p class="about">Sed ut perspiciatis unde omnis iste natus error sit voluptatem accusa ntium dolo remque laudantium consequuntur magni dolores eos qui ratione.</p>
  <div class="fcol" style="left:435px"><h4>SITE MAP</h4>Home<br>About<br>Meet The Team<br>Services<br>News<br>FAQs<br>Contact</div>
  <div class="fcol" style="left:667px"><h4>SERVICES</h4>PrEP<br>PeP<br>Hepatitis C<br>HIV<br>STI<br>Cas Management<br>Telehealth</div>
  <div class="fcol" style="left:886px;width:250px">
    <h4>SITE MAP</h4>
    <div class="sub">WELLSPRING CREST PARTNERS</div>
    <div class="crow"><b></b>Nemo enim ipsam volupta tem quia voluptas</div>
    <div class="crow"><b></b>+1-800-555-0142</div>
    <div class="crow"><b></b>+1-800-555-0142</div>
    <div class="crow"><b></b>info@wellspringcrest.org</div>
    <div class="fsocial"><span></span><span></span><span></span><span></span><span></span></div>
  </div>
  <div class="fline"></div>
  <div class="copyright">Copyright © 2022 Wellspring Crest Partners, Inc. All Right reserved</div>
</footer>

</body>
</html>
```